Awesome Professional Template for a collaborative report

File format: A4 PDF ideally

Design Requirements:

3 or 4 variants of a template some with graphics and pull quotes and a bio page for the essayists with a profile pic and a short descriptor

Layout Format: PPT would be perfect ideally portrait format

Style/Reference Guide: Varnholt or QM styles thought leadership reports as a guide

We need to input 10 essays around a specific subject with a nice layout with place holders for high impact pull quotes from the copy, stunning colourway and typrography probably A4 format but emailed as a PDF ideally not a huge file size. Striking front cover with title and list of contributors plus layout variations for the essays which will include a head shot short profile and contacts for the authors. Ideally a portrait format PPT that is easy to work with.

Target Market(s)

business professionals in brands

Industry/Entity Type

brand marketing

Font styles to use
Sans Serif

Colors
0054AA
0677BA
7BADD7
CADEEF
E8F1F8
00AB8E
00BBA5
67D7C9
C6EFE9
E9F9F6
F0912C
F2A743
F7CA91
FBE8D2
FDF5EE
6B429C
8869AF
B7A5CE
E3DAEB
F3F0F8

Requirements
Must have
• awesome visual impact

```html
<!DOCTYPE html>
<html lang="en">
<head>
<meta charset="utf-8">
<title>The Truth About New AI — Cover</title>
<link rel="stylesheet" href="https://fonts.googleapis.com/css2?family=IBM+Plex+Sans:wght@300;400;500;600;700&display=swap">
<style>
  :root {
    --paper: #ffffff;
    --ink: #111111;
    --navy: #061431;
    --purple-deep: #4a287c;
    --purple-veil: #5b3a8e;
    --cyan-ring: #4fc3d6;
    --art-light: #f4f5f6;
    --art-mid: #c9cccf;
    --text-light: #ffffff;
    --bar: #4a287c;
  }
  * { margin: 0; padding: 0; box-sizing: border-box; }
  html, body { width: 845px; height: 1200px; overflow: hidden; background: var(--paper); }
  body { font-family: "IBM Plex Sans", Arial, sans-serif; }
  .cover { position: relative; width: 845px; height: 1200px; overflow: hidden; background: var(--paper); }
  .cover-shapes { position: absolute; inset: 0; }
  .issue-date {
    position: absolute; left: 82px; top: 162px;
    transform: rotate(-90deg); transform-origin: left top;
    font-size: 15px; font-weight: 400; letter-spacing: 1px; color: var(--ink);
  }
  .project-tag {
    position: absolute; right: 82px; top: 92px;
    font-size: 19px; font-weight: 500; color: var(--ink);
  }
  .cover-title { position: absolute; left: 74px; top: 506px; color: var(--text-light); }
  .cover-title .kicker { display: block; font-size: 42px; font-weight: 300; line-height: 1; }
  .cover-title .headline { display: block; font-size: 89px; font-weight: 700; line-height: 1; margin-top: 10px; letter-spacing: 1px; }
  .cover-summary {
    position: absolute; left: 79px; top: 1071px; height: 64px;
    border-left: 8px solid var(--bar); padding-left: 16px; padding-top: 14px;
    color: var(--text-light); font-size: 14.5px; line-height: 1.25; font-weight: 400;
  }
</style>
</head>
<body>
<main class="cover">
  <svg class="cover-shapes" width="845" height="1200" viewBox="0 0 845 1200" aria-hidden="false">
    <defs>
      <radialGradient id="art-tone" cx="0.55" cy="0.45" r="0.6">
        <stop offset="0" stop-color="var(--art-mid)"/>
        <stop offset="1" stop-color="var(--art-light)"/>
      </radialGradient>
    </defs>
    <circle class="navy-arc" cx="-136" cy="1771" r="1128" fill="var(--navy)"/>
    <circle class="art-frame" cx="378" cy="596" r="381" fill="var(--paper)" stroke="var(--cyan-ring)" stroke-width="8"/>
    <circle class="art-fill" cx="378" cy="596" r="377" fill="url(#art-tone)" role="img" aria-label="Low-poly wireframe illustration of a human head dissolving into network nodes"/>
    <circle class="purple-veil" cx="20" cy="589" r="482" fill="var(--purple-veil)" opacity="0.92"/>
    <circle class="purple-disc" cx="0" cy="593" r="330" fill="var(--purple-deep)"/>
  </svg>

  <div class="issue-date">JUL 2023</div>
  <div class="project-tag">a collaborative project</div>

  <h1 class="cover-title">
    <span class="kicker">The Truth About</span>
    <span class="headline">NEW AI</span>
  </h1>

  <p class="cover-summary">15 expert essays about the {add adjective} nature of<br>current AI tech, by leading industry experts.</p>
</main>
</body>
</html>
```